Morrow Pike (we have a logo but are open to options ) (we hand make 100% soy candles & other hom

See our webpage for ideas www.morrowpike.com.
We need packaging for our Hearth Pots in 5 different fragrances to start with & need to be able to add new lines along the way.
The box needs to be uniformed and then adding what is required to reflect each fragrance as we add them on the line. Eg. Harbor Drift, Fig & Cedar, Desert Poppy, Oak & Amber, Sweet Peppermint (&; these could change).
There will also be matching boxes required for Reed Diffusers, Tealights and so on in our range.
-We want a white box, with a lux look, and kept simple. (We think an embossed logo might give it that lux look).
-We need to add things to our box like, warning instructions, burn instructions, barcodes etc.
-We are also changing our instragram account with our colour palette which will be backgrounds of white and pastel pinks, pink shades, some grey & black.
It's a chic lux sophicated look! Thank you.
16/06/18 We have just updated this brief. I have attached a colour palette picture. Ideally we would like the box to be white with embossed logo and maybe textured print on the sides or a chic print on the sides. The whole box appears to be too busy. It needs to look more feminine. On the colour palette, those colours could be used to write each different fragrance or the fragrance could be written in those colours. We hope this makes sense. We look forward to working with someone and hopefully we can use Skye or facetime to explain ourselves better. :)
Many Thanks, we hope you have fun with it.

Target Market(s)

People between ages of 18 to 50

Industry/Entity Type

Retail

Font styles to use
Sans Serif

Colors
ffffff
e667a6
eda3c7
f9d9e8
fdf0f6
959595
dbdbdb

Requirements
Must have
• Lux look with nice clean lines keeping it simple
• Obvioulsy, colours will change slightly when the box is introduced with a new fragrance to suit. Eg. Sweet Peppermint (yellow /green)
Nice to have
• Pattern for the fragrance to differ the uniformity of the boxes to the brand.
• 100% Soy Wax.

```html
<!DOCTYPE html>
<html lang="en">
<head>
<meta charset="utf-8">
<title>Morrow Pike – Hearth Pot Box Dieline</title>
<link rel="stylesheet" href="https://fonts.googleapis.com/css2?family=Montserrat:wght@400;500&display=swap">
<style>
  :root {
    --paper: #ffffff;
    --cut-line: #3a3a3a;
    --print-pink: #f0b8be;
    --brand-grey: #444444;
    --fragrance-pink: #eda3c7;
    --mark-pink: #f4b3b6;
  }
  html, body {
    margin: 0;
    padding: 0;
    width: 1200px;
    height: 752px;
    overflow: hidden;
    background: var(--paper);
  }
  .dieline {
    display: block;
    width: 1200px;
    height: 752px;
  }
  .cut { fill: none; stroke: var(--cut-line); stroke-width: 2; stroke-linejoin: miter; }
  .sheet-border { fill: var(--paper); stroke: var(--cut-line); stroke-width: 2; }
  .side-print { fill: var(--print-pink); }
  .brand-frame { fill: var(--paper); stroke: var(--brand-grey); stroke-width: 2; }
  .brand-square { fill: var(--mark-pink); }
  .brand-name {
    font-family: "Montserrat", sans-serif;
    font-weight: 500;
    font-size: 17px;
    letter-spacing: 6px;
    fill: var(--brand-grey);
  }
  .fragrance-name {
    font-family: "Montserrat", sans-serif;
    font-weight: 400;
    font-size: 19px;
    letter-spacing: 1.5px;
    fill: var(--fragrance-pink);
  }
  .fragrance-sub {
    font-family: "Montserrat", sans-serif;
    font-weight: 400;
    font-size: 12px;
    letter-spacing: 2px;
    fill: var(--fragrance-pink);
  }
</style>
</head>
<body>
<svg class="dieline" viewBox="0 0 1462 916" xmlns="http://www.w3.org/2000/svg">
  <rect class="sheet-border" x="1" y="1" width="1460" height="914"/>

  <!-- printed side panels -->
  <rect class="side-print" x="500" y="323" width="286" height="360" role="img" aria-label="Pastel pink side panel with small grey and pink flower pattern"/>
  <rect class="side-print" x="1072" y="321" width="288" height="362" role="img" aria-label="Pastel pink side panel with small grey and pink flower pattern"/>

  <!-- glue flap and back panel -->
  <path class="cut" d="M215 323 L177 338 L177 668 L215 683"/>
  <rect class="cut" x="215" y="323" width="285" height="360"/>

  <!-- top dust flaps -->
  <path class="cut" d="M500 323 L516 300 L544 156 L772 155 L772 300 L786 321"/>
  <path class="cut" d="M1072 321 L1087 300 L1087 154 L1313 154 L1343 300 L1360 321"/>

  <!-- lid -->
  <rect class="cut" x="787" y="36" width="285" height="285"/>

  <!-- main panels -->
  <rect class="cut" x="500" y="323" width="286" height="360"/>
  <rect class="cut" x="786" y="321" width="286" height="360"/>
  <path class="cut" d="M1072 321 L1360 321 L1360 683 L1072 683"/>

  <!-- bottom lock flaps -->
  <path class="cut" d="M215 683 L218 863 L314 862 L357 832 L357 822 L366 826 L400 862 L485 862 L488 695 L500 683 L366 826"/>
  <path class="cut" d="M500 683 L516 825 L686 825 L786 683"/>
  <path class="cut" d="M786 683 L790 863 L886 862 L930 832 L930 822 L938 826 L973 862 L1058 862 L1060 695 L1072 681 L938 826"/>
  <path class="cut" d="M1072 683 L1088 825 L1256 825 L1360 683"/>

  <!-- lid brand block -->
  <g class="brand-block">
    <rect class="brand-frame" x="855" y="93" width="146" height="145"/>
    <rect class="brand-square" x="911" y="111" width="34" height="60"/>
    <text class="brand-name" x="931" y="202" text-anchor="middle">MORROW</text>
    <text class="brand-name" x="931" y="222" text-anchor="middle">PIKE</text>
  </g>

  <!-- front brand block -->
  <g class="brand-block">
    <rect class="brand-frame" x="857" y="368" width="145" height="147"/>
    <rect class="brand-square" x="913" y="386" width="34" height="60"/>
    <text class="brand-name" x="932" y="478" text-anchor="middle">MORROW</text>
    <text class="brand-name" x="932" y="498" text-anchor="middle">PIKE</text>
  </g>

  <!-- fragrance -->
  <text class="fragrance-name" x="930" y="607" text-anchor="middle">HARBOR</text>
  <text class="fragrance-sub" x="930" y="623" text-anchor="middle">DRIFT</text>
</svg>
</body>
</html>
```